Multi Disciplinary Health Clinic Needs a Pop Up Banner

Brightpath Health needs a pop up banner ( approx. 33" x 80") to use at marketing events. We offer Chiropractic, Massage Therapy, Acupuncture, Laser Therapy, Shockwave Therapy and a lot of other modalities. We have a diverse client base ranging from children to professional athletes. More info about our clinic can be found at www.brightpathhealth.ca

Target Market(s)

potential patients, all age ranges, people who are in pain or are wanting to improve their health

Industry/Entity Type

Health And Wellness

Font styles to use
Sans Serif

Requirements
Must have
• our logo
• serives: chiropractic, massage therapy, shockwave, laser
• our logo colours as the basis for the colour theme
• our website address
Nice to have
• our phone number
• images from our website ( i have high resolution files of all images)
• word font that fits with our logo font
Should not have
• an abundance of spa massage pictures. we focus more on the rehabilitation of pain and injury.

```html
<!DOCTYPE html>
<html lang="en">
<head>
<meta charset="utf-8">
<title>Brightpath Health – Vertical Pop Up Banner</title>
<link href="https://fonts.googleapis.com/css2?family=Roboto+Condensed:ital,wght@0,400;0,700;0,900;1,400;1,700;1,900&family=Source+Sans+3:wght@400&display=swap" rel="stylesheet">
<style>
  :root {
    --brand-orange: #ee5a24;
    --brand-blue: #1f5fa8;
    --slate: #5a5d63;
    --sky-top: #ffffff;
    --sky-bottom: #aecbea;
    --photo-light: #9dbf86;
    --photo-dark: #55863c;
    --label-grey: #77787b;
    --white: #ffffff;
  }
  * { margin: 0; padding: 0; box-sizing: border-box; }
  html, body {
    width: 1200px; height: 1000px; overflow: hidden;
    background: var(--white);
    font-family: "Roboto Condensed", Arial, sans-serif;
  }
  .stage { position: relative; width: 1200px; height: 1000px; }

  .banner {
    position: absolute; left: 233px; top: 17px; width: 397px; height: 961px;
    background: linear-gradient(180deg, var(--sky-top) 0%, #dbe7f4 12%, var(--sky-bottom) 35%, var(--sky-bottom) 100%);
    box-shadow: 4px 6px 8px rgba(0,0,0,0.28);
    overflow: hidden;
  }
  .banner-cap { position: absolute; left: 0; width: 397px; height: 40px; z-index: 3; }
  .banner-cap--top { top: 0; }
  .banner-cap--bottom { bottom: 0; }

  .brand {
    position: absolute; top: 62px; left: 0; width: 397px;
    display: flex; align-items: center; justify-content: center; gap: 12px;
  }
  .brand-dot { width: 34px; height: 34px; border-radius: 50%; background: var(--brand-blue); }
  .brand-name { font-size: 37px; font-weight: 700; color: var(--brand-blue); letter-spacing: 0.5px; }

  .tagline { position: absolute; top: 154px; left: 0; width: 397px; text-align: center; color: var(--brand-orange); font-style: italic; }
  .tagline-lead { font-size: 34px; font-weight: 400; line-height: 34px; }
  .tagline-main { font-size: 52px; font-weight: 900; line-height: 70px; letter-spacing: 0.5px; }

  .services { position: absolute; top: 267px; left: 0; width: 397px; list-style: none; text-align: center; }
  .services li { font-size: 27px; font-weight: 700; color: var(--slate); line-height: 38.3px; }

  .book-now {
    position: absolute; top: 493px; left: 0; width: 207px; height: 31px;
    background: var(--brand-orange); border-radius: 0 8px 8px 0;
    color: var(--white); font-size: 20px; font-weight: 900; letter-spacing: 6px;
    line-height: 31px; padding-left: 23px;
  }

  .contact { position: absolute; top: 533px; left: 23px; font-size: 17.5px; font-weight: 700; line-height: 26px; z-index: 2; }
  .contact-line--primary { color: var(--slate); }
  .contact-line--address { color: var(--brand-orange); }

  .hero-photo {
    position: absolute; top: 612px; left: 0; width: 397px; height: 349px;
    background: linear-gradient(180deg, var(--photo-light) 0%, var(--photo-dark) 100%);
  }

  .hero-caption {
    position: absolute; top: 872px; left: 121px; width: 300px; text-align: center;
    color: var(--white); font-size: 22px; font-weight: 700; font-style: italic; line-height: 21px;
    text-shadow: 0 1px 3px rgba(0,0,0,0.45); z-index: 2;
  }

  .spec-label {
    position: absolute; left: 760px; top: 672px; width: 230px; text-align: center;
    font-family: "Source Sans 3", Arial, sans-serif; font-size: 46px; line-height: 57px;
    color: var(--label-grey);
  }
</style>
</head>
<body>
<div class="stage">
  <div class="banner">
    <svg class="banner-cap banner-cap--top" viewBox="0 0 397 40" preserveAspectRatio="none" aria-hidden="true">
      <path d="M0 0 H397 V24 Q200 40 0 36 Z" fill="var(--brand-orange)"/>
    </svg>

    <div class="brand">
      <span class="brand-dot"></span>
      <span class="brand-name">Brightpath Health</span>
    </div>

    <div class="tagline">
      <p class="tagline-lead">HELPING YOU LIVE LIFE</p>
      <p class="tagline-main">PAIN FREE!</p>
    </div>

    <ul class="services">
      <li>Chiropractic</li>
      <li>Massage</li>
      <li>Acupuncture</li>
      <li>Shockwave Treatment</li>
      <li>Laser Therapy</li>
    </ul>

    <div class="book-now">BOOK NOW</div>

    <div class="contact">
      <p class="contact-line--primary">(403) 555-0147 • WWW.BRIGHTPATHHEALTH.CA</p>
      <p class="contact-line--address">1480 MAPLE RIDGE PARKWAY NW, SUITE 210</p>
      <p class="contact-line--address">CALGARY, ALBERTA T3P 1A4</p>
    </div>

    <div class="hero-photo" role="img" aria-label="Photo of a happy family of four running hand in hand across a green grassy field"></div>

    <p class="hero-caption">From children<br>to professional athletes</p>

    <svg class="banner-cap banner-cap--bottom" viewBox="0 0 397 40" preserveAspectRatio="none" aria-hidden="true">
      <path d="M0 4 Q200 -2 397 10 V40 H0 Z" fill="var(--brand-orange)"/>
    </svg>
  </div>

  <div class="spec-label">33″ X 80″<br>VERTICAL<br>BANNER</div>
</div>
</body>
</html>
```